Kitchen manufaturer business card/logo design

I am a small kitchen manufacturing company that makes and installs all sorts of cabinetry.

The colours im looking to incorporate in the card are light/baby blue, white and black.

Incorporate 5 stars to show quality workmanship and product.

Looking for a modern classy design.
Updates

Hey guys, New idea. The logo should be made using HK in the most modern way possible as well as the full company name below it. Thanks.

Target Market(s)

Anyone with a home thats looking for a new cabinetry of any sort.

Industry/Entity Type

Business

Contact Information for Business Card

Harbor Kitchens
Tod Villaran
PH 0431 582 904
Email- harborkitchens@mailvane.example
ABN- 73 208 561 339
-Kitchens
-Vanities
-Laundries
-Media Units
-Studies
-Wardrobes
-3D Computer Designs

Requirements
Must have

• The front of the card must only have the company name.
The different types of cabinetry I do must be on the back of the card in point form but instead of using points use stars.
Nice to have
• Just think classy and quality

```html
<!DOCTYPE html>
<html lang="en">
<head>
<meta charset="utf-8">
<title>Harbor Kitchens – Business Card</title>
<link href="https://fonts.googleapis.com/css2?family=Lato:wght@400;700;900&family=Black+Ops+One&display=swap" rel="stylesheet">
<style>
  :root {
    --page-bg: #e9e7e3;
    --card-black: #0b0b0c;
    --card-white: #ffffff;
    --ink: #141414;
    --brand-blue: #3b6fc0;
    --muted: #2a2a2a;
  }
  * { box-sizing: border-box; margin: 0; padding: 0; }
  html, body {
    width: 1200px;
    height: 1000px;
    overflow: hidden;
    background: var(--page-bg);
    font-family: "Lato", Arial, sans-serif;
  }
  .sheet {
    width: 1200px;
    height: 1000px;
    display: flex;
    flex-direction: column;
    align-items: center;
    justify-content: center;
    gap: 30px;
  }
  .card {
    position: relative;
    width: 800px;
    height: 457px;
    overflow: hidden;
    box-shadow: 0 6px 18px rgba(0,0,0,0.18);
  }

  /* Front */
  .card-front {
    background: linear-gradient(135deg, #1a1a1c 0%, var(--card-black) 45%, #000 100%);
    display: flex;
    align-items: center;
    justify-content: center;
  }
  .front-wordmark {
    font-family: "Lato", Arial, sans-serif;
    font-weight: 900;
    font-size: 58px;
    letter-spacing: 1px;
    color: var(--card-white);
  }

  /* Back */
  .card-back {
    background: var(--card-white);
    color: var(--ink);
  }
  .back-wordmark {
    position: absolute;
    top: 62px;
    right: 52px;
    font-family: "Lato", Arial, sans-serif;
    font-weight: 900;
    font-size: 32px;
    color: var(--ink);
  }
  .services {
    position: absolute;
    top: 122px;
    right: 52px;
    list-style: none;
    text-align: right;
    font-size: 17px;
    line-height: 23px;
    color: var(--ink);
  }
  .services li {
    display: flex;
    justify-content: flex-end;
    align-items: center;
    gap: 6px;
  }
  .services li.no-star { padding-right: 22px; margin-top: 14px; }
  .star-bullet { width: 16px; height: 16px; fill: var(--brand-blue); }
  .holder-name {
    position: absolute;
    top: 212px;
    left: 56px;
    font-family: "Black Ops One", Impact, sans-serif;
    font-size: 30px;
    color: var(--brand-blue);
  }
  .contact {
    position: absolute;
    left: 56px;
    bottom: 54px;
    font-size: 17px;
    line-height: 25px;
    color: var(--muted);
  }
  .contact .label { color: var(--brand-blue); }
  .accent-band {
    position: absolute;
    right: 0;
    bottom: 0;
    width: 330px;
    height: 12px;
    background: var(--brand-blue);
    clip-path: polygon(10px 0, 100% 0, 100% 100%, 0 100%);
  }
</style>
</head>
<body>
<main class="sheet">
  <section class="card card-front" aria-label="Card front">
    <div class="front-wordmark">Harbor Kitchens</div>
  </section>

  <section class="card card-back" aria-label="Card back">
    <div class="back-wordmark">Harbor Kitchens</div>

    <svg width="0" height="0" style="position:absolute">
      <defs>
        <symbol id="star" viewBox="0 0 24 24">
          <path d="M12 1.5l3.1 7.1 7.7.7-5.8 5.1 1.7 7.6L12 18l-6.7 4 1.7-7.6-5.8-5.1 7.7-.7z"/>
        </symbol>
      </defs>
    </svg>

    <ul class="services">
      <li>Kitchens <svg class="star-bullet"><use href="#star"/></svg></li>
      <li>Vanities <svg class="star-bullet"><use href="#star"/></svg></li>
      <li>Laundries <svg class="star-bullet"><use href="#star"/></svg></li>
      <li>Media Units <svg class="star-bullet"><use href="#star"/></svg></li>
      <li>Studies <svg class="star-bullet"><use href="#star"/></svg></li>
      <li>Wardrobes <svg class="star-bullet"><use href="#star"/></svg></li>
      <li class="no-star">3D Computer Designs</li>
    </ul>

    <div class="holder-name">Tod Villaran</div>

    <div class="contact">
      <p><span class="label">Phone:</span> 0431 582 904</p>
      <p><span class="label">Email:</span> harborkitchens@mailvane.example</p>
      <p><span class="label">ABN:</span> 73 208 561 339</p>
    </div>

    <div class="accent-band"></div>
  </section>
</main>
</body>
</html>
```